Business Card Design Project

Professional business cards for law firm - a rough example of what we are looking for is attached. The logo, colour and styling of the name are all new and dont need to be changed. We need layout for front and back. We are looking for some imaginative layout of info. We are a young vibrant firm and not too conservative and are not adverse to something quite different.
Updates

Thank you for all the submissions.  We have been blown away with the quality of your work.  Our management team will be meeting later in the week to make our decision.  Again, thanks for the fabulous work.

Industry/Entity Type

Conservative

Requirements
Must have
• Logo and name as in attached example (colour and font)
Should not have
• Scales of Justice

```html
<!DOCTYPE html>
<html lang="en">
<head>
<meta charset="utf-8">
<title>Harlow Vance Legal – Business Card</title>
<link rel="stylesheet" href="https://fonts.googleapis.com/css2?family=Oxygen:wght@400;700&family=Oswald:wght@600&family=Didact+Gothic&display=swap">
<style>
  :root {
    --canvas: #ffffff;
    --navy-deep: #1b3487;
    --navy: #1d4a9a;
    --blue-glow: #1a82b8;
    --gold: #fad83a;
    --white: #ffffff;
    --soft-white: #dfe9f5;
    --rule: #6f9fcf;
    --band-text: #1c2a6b;
  }
  * { margin: 0; padding: 0; box-sizing: border-box; }
  html, body { width: 1200px; height: 900px; overflow: hidden; background: var(--canvas); }
  .canvas { position: relative; width: 1200px; height: 900px; }

  .card {
    position: absolute;
    width: 572px; height: 323px;
    overflow: hidden;
    box-shadow: 3px 5px 8px rgba(0,0,0,0.35);
  }
  .card-front {
    left: 50px; top: 240px;
    border-radius: 162px 0 0 162px;
    background: radial-gradient(ellipse 60% 75% at 50% 50%, var(--blue-glow) 0%, var(--navy) 55%, var(--navy-deep) 100%);
  }
  .card-back {
    left: 610px; top: 325px; width: 552px;
    border-radius: 0 162px 162px 0;
    background: radial-gradient(ellipse 55% 70% at 55% 45%, var(--blue-glow) 0%, var(--navy) 55%, var(--navy-deep) 100%);
  }

  .front-ring {
    position: absolute; left: 18px; top: 15px;
    width: 294px; height: 294px; border-radius: 50%;
    border: 2px solid rgba(255,255,255,0.12);
  }

  .firm-name {
    position: absolute; left: 232px; top: 104px; width: 320px;
    font-family: "Oxygen", sans-serif; font-weight: 400;
    color: var(--gold); text-align: right;
  }
  .firm-name .line-main { display: block; font-size: 47px; line-height: 52px; }
  .firm-name .line-sub {
    display: block; font-size: 25px; line-height: 28px;
    letter-spacing: 4px; margin-right: 100px; text-align: right;
  }
  .tagline {
    position: absolute; left: 281px; top: 192px;
    font-family: "Oxygen", sans-serif; font-style: italic;
    font-size: 14.5px; color: var(--soft-white);
  }
  .front-rule {
    position: absolute; left: 295px; top: 227px; width: 210px; height: 1px;
    background: var(--rule);
  }
  .person-name {
    position: absolute; left: 243px; top: 238px; width: 310px; text-align: center;
    font-family: "Oswald", sans-serif; font-weight: 600; font-size: 27px;
    line-height: 34px; color: var(--gold); letter-spacing: -0.3px;
  }
  .person-role {
    position: absolute; left: 243px; top: 274px; width: 310px; text-align: center;
    font-family: "Didact Gothic", sans-serif; font-size: 13px;
    letter-spacing: 4px; color: var(--white);
  }

  .practice-band {
    position: absolute; left: 0; top: 29px; width: 100%; height: 52px;
    background: var(--gold);
    padding: 7px 0 0 20px;
    font-family: "Didact Gothic", sans-serif; font-size: 15.5px;
    line-height: 19px; color: var(--band-text);
  }
  .contact-list {
    position: absolute; left: 26px; top: 186px; list-style: none;
    font-family: "Didact Gothic", sans-serif; font-size: 15px; color: var(--white);
  }
  .contact-list li { display: flex; align-items: center; height: 17.5px; }
  .contact-list li.with-icon { height: 21px; }
  .contact-list svg { width: 14px; height: 14px; margin-right: 7px; flex-shrink: 0; }
</style>
</head>
<body>
<div class="canvas">

  <section class="card card-front" aria-label="Card front">
    <div class="front-ring"></div>
    <h1 class="firm-name">
      <span class="line-main">Harlow Vance</span>
      <span class="line-sub">LEGAL</span>
    </h1>
    <p class="tagline">helping you find the way forward</p>
    <div class="front-rule"></div>
    <p class="person-name">Eleanor Marsh LLB BA</p>
    <p class="person-role">Solicitor</p>
  </section>

  <section class="card card-back" aria-label="Card back">
    <div class="practice-band">
      Family . Restraining Orders . Probate/Wills . Dividing Fences<br>
      Traffic . Criminal . Debt Recovery . Financial Agreements
    </div>
    <ul class="contact-list">
      <li>4/82 Carrington Street, Ashfield WA 6054</li>
      <li>PO Box 517, Ashfield WA 6954</li>
      <li class="with-icon">
        <svg viewBox="0 0 14 14" aria-hidden="true"><path fill="#fff" d="M1 5c0-2 2-3 6-3s6 1 6 3v1h-3V5H4v1H1z M3 7h8l1 5H2z"/><circle cx="7" cy="9.3" r="1.4" fill="#1d4a9a"/></svg>
        9412 0357, 6120 4418
      </li>
      <li class="with-icon">
        <svg viewBox="0 0 14 14" aria-hidden="true"><path fill="#fff" d="M4 3l2-2v3h2l1 1v8H5l-1-1z"/></svg>
        6300 1847
      </li>
      <li class="with-icon">
        <svg viewBox="0 0 14 14" aria-hidden="true"><rect x="1" y="3" width="12" height="9" fill="none" stroke="#fff" stroke-width="1.3"/><path d="M1 3l6 5 6-5" fill="none" stroke="#fff" stroke-width="1.3"/></svg>
        reception@harlowvancelegal.com.au
      </li>
    </ul>
  </section>

</div>
</body>
</html>
```